Blue-otter-nest.com

The existing website http://www.blue-otter-nest.com needs to get into shape. I'd like to have it transformed into wordpress with a brand-new design. The design should include a logo for multiple uses.

```html
<!DOCTYPE html>
<html lang="en">
<head>
<meta charset="utf-8">
<title>Blue Otter Nest</title>
<link href="https://fonts.googleapis.com/css2?family=Arimo:wght@400;700&family=Open+Sans:wght@400;700&display=swap" rel="stylesheet">
<style>
:root{
  --red:#e8403f;
  --ink:#2b2b2b;
  --muted:#6c6c6c;
  --footer:#2a2424;
  --footer-line:#3a3333;
  --white:#ffffff;
}
*{margin:0;padding:0;box-sizing:border-box}
html,body{width:1200px;height:2219px;overflow:hidden;background:var(--white)}
body{position:relative;font-family:"Open Sans",Arial,sans-serif;color:var(--ink)}
.abs{position:absolute}
.heading{font-family:"Arimo",Arial,sans-serif;font-weight:700;text-transform:uppercase}

/* header */
.topline{left:0;top:0;width:1200px;height:5px;background:var(--red)}
.phone-tab{left:858px;top:0;width:248px;height:34px;background:var(--red);color:var(--white);
  font-size:15px;font-weight:700;display:flex;align-items:center;justify-content:center;gap:10px;
  clip-path:polygon(0 0,100% 0,94% 100%,6% 100%)}
.brand{left:99px;top:30px;display:flex;align-items:center;gap:12px}
.brand-dot{width:40px;height:40px;border-radius:50%;background:var(--red)}
.brand-name{font-family:"Arimo",Arial,sans-serif;font-weight:700;font-size:19px;color:var(--ink);text-transform:uppercase}
.nav{left:465px;top:60px;font-family:"Arimo",Arial,sans-serif;font-weight:700;font-size:14px;text-transform:uppercase}
.nav span{position:absolute;white-space:nowrap}
.nav .active::after{content:"";position:absolute;left:50%;top:28px;margin-left:-8px;border:8px solid transparent;border-bottom-color:var(--red)}

/* hero */
.hero{left:0;top:95px;width:1200px;height:433px;background:linear-gradient(180deg,#c9c8c4 0%,#a9a7a3 45%,#55565a 75%,#3e3f44 100%)}
.hero-kicker{left:0;top:230px;width:1200px;text-align:center;color:var(--white);font-size:25px;text-shadow:0 2px 4px rgba(0,0,0,.5)}
.hero-title{left:0;top:270px;width:1200px;text-align:center;color:var(--white);font-size:40px;text-shadow:0 2px 5px rgba(0,0,0,.6)}
.circle{border-radius:50%;background:#222}
.hero-arrow{top:296px;width:14px;height:26px}

/* intro */
.intro-title{left:0;top:571px;width:1200px;text-align:center;font-size:22px}
.intro-text{left:260px;top:616px;width:680px;text-align:center;font-size:12.5px;line-height:24px;color:var(--muted)}
.video{left:207px;top:697px;width:786px;height:404px;background:#2b2b2b}
.video-art{left:0;top:0;width:786px;height:365px;background:linear-gradient(180deg,#f5f5f5,#e9e9e9)}
.video-title{left:12px;top:9px;color:var(--white);font-size:15px;font-family:"Arimo",Arial,sans-serif}
.video-bar{left:0;top:365px;width:786px;height:39px;background:#1c1c1c}

/* features */
.features{left:0;top:1148px;width:1200px;height:364px;background:var(--red)}
.feature{width:296px;text-align:center;color:var(--white)}
.feature h3{font-family:"Arimo",Arial,sans-serif;font-size:17px;text-transform:uppercase;margin:0 -40px 12px}
.feature p{font-size:11.5px;line-height:22px;height:66px}
.feature .more{display:block;font-size:11.5px;font-weight:700;margin-top:14px}

/* about */
.about-title{left:98px;top:1554px;font-size:22px}
.about-text{left:98px;width:566px;font-size:12px;line-height:24px;color:var(--muted)}
.read-more{left:98px;top:1824px;font-size:11.5px;font-weight:700;color:var(--red)}
.plan-img{left:690px;top:1554px;width:411px;height:299px;background:linear-gradient(180deg,#1f8e5a 0 13%,#f3f6f4 13% 100%);border:3px solid #1f8e5a}

/* footer */
.footer{left:0;top:1894px;width:1200px;height:256px;background:var(--footer)}
.f-head{top:1926px;color:var(--white);font-size:14.5px}
.f-links{top:1962px;color:#d9d6d6;font-size:12px;line-height:20.7px;list-style:none}
.f-text{color:#d9d6d6;font-size:12px;line-height:21px}
.email-input{left:302px;top:2010px;width:274px;height:39px;background:#3a3333;border:1px solid #4a4242;color:#8c8585;font-size:12px;padding:0 12px;line-height:37px}
.subscribe{left:302px;top:2067px;width:96px;height:35px;border:2px solid var(--red);color:var(--white);font-size:11.5px;font-weight:700;text-align:center;line-height:31px}
.bottom{left:0;top:2152px;width:1200px;height:67px;background:var(--red)}
.copyright{left:99px;top:2175px;color:var(--white);font-size:12px}
.wcircle{border-radius:50%;background:var(--white)}
</style>
</head>
<body>

<header>
  <div class="abs topline"></div>
  <div class="abs phone-tab">
    <svg width="13" height="13" viewBox="0 0 24 24"><path fill="#fff" d="M6.6 10.8a15.1 15.1 0 0 0 6.6 6.6l2.2-2.2c.3-.3.7-.4 1-.2 1.1.4 2.3.6 3.6.6.6 0 1 .4 1 1V20c0 .6-.4 1-1 1A17 17 0 0 1 3 4c0-.6.4-1 1-1h3.5c.6 0 1 .4 1 1 0 1.3.2 2.5.6 3.6.1.3 0 .7-.2 1z"/></svg>
    +49 (0) 5120/41 62 30 0
  </div>
  <div class="abs brand">
    <div class="brand-dot"></div>
    <div class="brand-name">Blue Otter Nest</div>
  </div>
  <nav class="abs nav">
    <span class="active" style="left:0">Claim</span>
    <span style="left:69px">Process</span>
    <span style="left:159px">Responsibility</span>
    <span style="left:295px">Costs</span>
    <span style="left:368px">Finishing</span>
    <span style="left:461px">Contact</span>
    <span style="left:554px">Blog</span>
  </nav>
  <svg class="abs" style="left:1083px;top:60px" width="17" height="17" viewBox="0 0 24 24"><circle cx="10" cy="10" r="7" fill="none" stroke="#2b2b2b" stroke-width="3"/><path d="M15 15l6 6" stroke="#2b2b2b" stroke-width="3.5" stroke-linecap="round"/></svg>
</header>

<section>
  <div class="abs hero" role="img" aria-label="Photo of a bright open-plan office with desks and chairs"></div>
  <svg class="abs hero-arrow" style="left:37px" viewBox="0 0 14 26"><path d="M12 2L2 13l10 11" fill="none" stroke="#fff" stroke-width="2.5" opacity=".8"/></svg>
  <svg class="abs hero-arrow" style="left:1148px" viewBox="0 0 14 26"><path d="M2 2l10 11L2 24" fill="none" stroke="#fff" stroke-width="2.5" opacity=".8"/></svg>
  <div class="abs hero-kicker heading">Blue Otter Nest</div>
  <h1 class="abs hero-title heading">A Company of Northwind Holding</h1>
  <div class="abs circle" style="left:503px;top:333px;width:54px;height:54px"></div>
  <div class="abs circle" style="left:572px;top:333px;width:54px;height:54px"></div>
  <div class="abs circle" style="left:640px;top:333px;width:54px;height:54px"></div>
</section>

<section>
  <h2 class="abs intro-title heading">What is a fire service plan?</h2>
  <p class="abs intro-text">It is burning. Now it is: get out of the building. To safety. Escape and rescue plans are an important guide and also an essential tool for training people for the right behavior in case of fire.</p>
  <div class="abs video">
    <div class="abs video-art" role="img" aria-label="Sketch-style explainer illustration of a fire engine, firefighters and safety signs"></div>
    <div class="abs" style="left:0;top:0;width:786px;height:40px;background:linear-gradient(180deg,rgba(0,0,0,.75),rgba(0,0,0,0))"></div>
    <div class="abs video-title">Was ist ein Feuerwehrplan?</div>
    <svg class="abs" style="left:365px;top:159px" width="56" height="56" viewBox="0 0 56 56"><circle cx="28" cy="28" r="28" fill="rgba(0,0,0,.55)"/><path d="M22 17l18 11-18 11z" fill="#fff"/></svg>
    <div class="abs" style="left:0;top:359px;width:786px;height:6px;background:#555"></div>
    <div class="abs" style="left:0;top:359px;width:36px;height:6px;background:var(--red)"></div>
    <div class="abs video-bar">
      <svg class="abs" style="left:30px;top:12px" width="120" height="16" viewBox="0 0 120 16"><path d="M2 1l12 7-12 7z" fill="#fff"/><rect x="32" y="1" width="4" height="14" fill="#fff"/><rect x="40" y="1" width="4" height="14" fill="#fff"/><rect x="62" y="1" width="13" height="14" fill="#fff"/><path d="M94 5h4l5-4v14l-5-4h-4z" fill="#fff"/></svg>
      <div class="abs" style="left:154px;top:11px;color:#fff;font-size:12px">1.08/12.06</div>
      <svg class="abs" style="left:690px;top:11px" width="80" height="18" viewBox="0 0 80 18"><path d="M0 12h4l5 4V2L4 6H0z" fill="#fff"/><path d="M56 1h7M56 1v6M79 1h-7M79 1v6M56 17h7M56 17v-6M79 17h-7M79 17v-6" stroke="#fff" stroke-width="2.5" fill="none"/></svg>
    </div>
  </div>
</section>

<section>
  <div class="abs features"></div>
  <svg class="abs" style="left:152px;top:1182px" width="170" height="136" viewBox="0 0 170 136" fill="none" stroke="#fff" stroke-width="2">
    <circle cx="50" cy="50" r="36"/><circle cx="50" cy="50" r="14"/>
    <circle cx="104" cy="100" r="24"/><circle cx="104" cy="100" r="9"/>
    <circle cx="150" cy="74" r="16"/><circle cx="150" cy="74" r="6"/>
  </svg>
  <svg class="abs" style="left:540px;top:1184px" width="118" height="118" viewBox="0 0 118 118" fill="none" stroke="#fff" stroke-width="2">
    <circle cx="59" cy="59" r="54"/><circle cx="59" cy="59" r="38"/><path d="M40 60l13 13 26-28"/>
  </svg>
  <svg class="abs" style="left:898px;top:1180px" width="128" height="128" viewBox="0 0 128 128" fill="none" stroke="#fff" stroke-width="2">
    <circle cx="60" cy="68" r="54"/><circle cx="60" cy="68" r="40"/><circle cx="60" cy="68" r="26"/><circle cx="60" cy="68" r="12"/><path d="M60 68l52-52M100 16h12v12"/>
  </svg>
  <div class="abs feature" style="left:90px;top:1346px">
    <h3>The demands on our work</h3>
    <p>The function of the escape and rescue plan is with us at any time at the center. We are aware that we can contribute with our work</p>
    <span class="more">READ MORE &gt;&gt;</span>
  </div>
  <div class="abs feature" style="left:451px;top:1346px">
    <h3>Our quality guarantee</h3>
    <p>We understand our craft. Our experts for fire pro&shy;tection as well as our technical draftsman and designer. Since 2001 we design..</p>
    <span class="more">READ MORE &gt;&gt;</span>
  </div>
  <div class="abs feature" style="left:812px;top:1346px">
    <h3>Success factor</h3>
    <p>Draw? That's part of it. But only individual program&shy;ming project - in DraftLine or Meridian PlanStudio - provide real performance! rescue plans.</p>
    <span class="more">READ MORE &gt;&gt;</span>
  </div>
</section>

<section>
  <h2 class="abs about-title heading">What are escape and rescue plans?</h2>
  <p class="abs about-text" style="top:1608px">It is burning. Now it is: get out of the building. To safety. Escape and rescue plans are an important guide and also an essential tool for training people for the right behavior in case of fire. With the pro&shy;fessional preparation of escape and rescue plans we contribute our part in ensuring that people with you in case of a fire in the shortest find ways out of the building.</p>
  <p class="abs about-text" style="top:1731px">Escape and rescue plans are - regulated by law - to update every two years. Since October 2012 also applies the new DIN EN ISO 7010 and DIN ISO 23601 We are happy to check for you whether your plans comply with this standard.</p>
  <div class="abs read-more">READ MORE &gt;&gt;</div>
  <div class="abs plan-img" role="img" aria-label="Example of a printed escape and rescue plan with floor layout and legend"></div>
</section>

<footer>
  <div class="abs footer"></div>
  <div class="abs" style="left:247px;top:1935px;width:1px;height:170px;background:var(--footer-line)"></div>
  <div class="abs" style="left:651px;top:1935px;width:1px;height:170px;background:var(--footer-line)"></div>
  <div class="abs" style="left:852px;top:1935px;width:1px;height:170px;background:var(--footer-line)"></div>

  <div class="abs f-head heading" style="left:99px">Company</div>
  <ul class="abs f-links" style="left:99px"><li>Claim</li><li>Process</li><li>Responsibility</li><li>Costs</li><li>Finishing</li><li>Contact</li><li>Blog</li></ul>

  <div class="abs f-head heading" style="left:302px">Newsletter</div>
  <p class="abs f-text" style="left:302px;top:1960px;width:230px">Register your Email Address to get informaiton about us</p>
  <div class="abs email-input">Email Address</div>
  <div class="abs subscribe">SUBSCRIBE</div>

  <div class="abs f-head heading" style="left:682px">Legal</div>
  <ul class="abs f-links" style="left:684px;line-height:24px"><li>Privacy</li><li>Legal Notice</li><li>Site Map</li><li>Terms &amp; Conditions</li></ul>

  <div class="abs f-head heading" style="left:916px">Contact Us</div>
  <svg class="abs" style="left:918px;top:1967px" width="11" height="15" viewBox="0 0 12 16"><path d="M6 0a6 6 0 0 0-6 6c0 4.5 6 10 6 10s6-5.5 6-10a6 6 0 0 0-6-6zm0 8.5A2.5 2.5 0 1 1 6 3.5a2.5 2.5 0 0 1 0 5z" fill="#fff"/></svg>
  <p class="abs f-text" style="left:942px;top:1964px">Blue-Otter-Nest<br>&nbsp;&nbsp;&nbsp;&nbsp;118 Harbor Court - Suite 210</p>
  <svg class="abs" style="left:918px;top:2037px" width="13" height="13" viewBox="0 0 24 24"><path fill="#fff" d="M6.6 10.8a15.1 15.1 0 0 0 6.6 6.6l2.2-2.2c.3-.3.7-.4 1-.2 1.1.4 2.3.6 3.6.6.6 0 1 .4 1 1V20c0 .6-.4 1-1 1A17 17 0 0 1 3 4c0-.6.4-1 1-1h3.5c.6 0 1 .4 1 1 0 1.3.2 2.5.6 3.6.1.3 0 .7-.2 1z"/></svg>
  <p class="abs f-text" style="left:942px;top:2033px">+49 (0) 5120/41 62 30 0</p>
  <svg class="abs" style="left:918px;top:2082px" width="16" height="12" viewBox="0 0 16 12"><rect width="16" height="12" rx="1" fill="#fff"/><path d="M1 1l7 6 7-6" stroke="#2a2424" stroke-width="1.4" fill="none"/></svg>
  <p class="abs f-text" style="left:950px;top:2078px;text-decoration:underline">info@blue-otter-nest.com</p>

  <div class="abs bottom"></div>
  <p class="abs copyright">Copyrights © 2016, BlueOtterNest. All Rights Reserved.</p>
  <div class="abs wcircle" style="left:986px;top:2166px;width:34px;height:34px"></div>
  <div class="abs wcircle" style="left:1026px;top:2166px;width:34px;height:34px"></div>
  <div class="abs wcircle" style="left:1066px;top:2166px;width:34px;height:34px"></div>
</footer>

</body>
</html>
```